The Velvet Magpie business card

I need a business card for my makeup artist business. I specialise in bridal, glamour, formal and special occasion makeup.
I am a mobile makeup artist who caters for every from nowra to sydney.
I do the following services:
Bridal makeup
airbrush makeup
special occasion
formals
hens nights/ girls night
makeup lesson
makeup for all ages from flower girl to Nanna of the bride!
photoshoot makeup
SPFX

I would like the card to portray a very professional sleek makeup business. I would also like another version of the card directed especially towards brides.

Please see my website to understand colours etc www.thevelvetmagpie.com

The Velvet Magpie
Professional Makeup Artist
Marisol Dunkel
0471829304
info@thevelvetmagpie.com
www.thevelvetmagpie.com
www.facebook.com/thevelvetmagpie

```html
<!DOCTYPE html>
<html lang="en">
<head>
<meta charset="utf-8">
<title>The Velvet Magpie – Business Card</title>
<link href="https://fonts.googleapis.com/css2?family=Roboto+Condensed:wght@300;400;700&display=swap" rel="stylesheet">
<style>
  :root {
    --magenta: #e0137f;
    --magenta-soft: #f06aa9;
    --ink: #3a3a3a;
    --paper: #ffffff;
    --backdrop: #d9d9d9;
    --photo-blue: #3a4fb8;
    --photo-warm: #c9a17f;
    --photo-skin: #d8b49a;
    --photo-dark: #5b4a42;
  }
  * { box-sizing: border-box; margin: 0; padding: 0; }
  html, body { width: 1200px; height: 748px; overflow: hidden; }
  body {
    background: var(--backdrop);
    font-family: "Roboto Condensed", "Arial Narrow", sans-serif;
    color: var(--ink);
    display: flex;
    align-items: center;
    justify-content: center;
    gap: 60px;
  }
  .card {
    width: 370px;
    height: 640px;
    background: var(--paper);
    position: relative;
    overflow: hidden;
    border-top: 7px solid var(--magenta);
  }

  /* Front */
  .brand {
    margin: 36px 0 0;
    text-align: center;
    font-weight: 700;
    font-size: 30px;
    letter-spacing: 3px;
    text-transform: uppercase;
    color: var(--magenta);
  }
  .identity { margin: 48px 0 0 34px; }
  .identity .name { font-size: 24px; font-weight: 300; color: var(--ink); }
  .identity .role { font-size: 15px; color: var(--magenta); margin-top: 2px; }
  .contacts { list-style: none; margin: 44px 0 0 34px; }
  .contacts li {
    display: flex; align-items: center; gap: 9px;
    font-size: 18px; font-weight: 300; margin-bottom: 9px;
  }
  .contacts svg { width: 20px; height: 20px; flex: none; }
  .ornament {
    position: absolute; left: 0; bottom: 0;
    width: 100%; height: 210px;
    background: radial-gradient(ellipse at 25% 75%, var(--magenta-soft) 0%, rgba(240,106,169,0.35) 45%, rgba(255,255,255,0) 75%);
  }

  /* Back */
  .collage {
    position: absolute; inset: 0;
    display: grid;
    grid-template-columns: 1fr 1fr;
    grid-template-rows: 205px 210px 1fr;
    gap: 8px;
    background: var(--magenta);
    padding: 0 0 0 0;
  }
  .photo { width: 100%; height: 100%; }
  .photo--party { grid-column: 1 / 3; background: linear-gradient(180deg, var(--photo-dark) 0%, var(--photo-blue) 60%, #2b3a8c 100%); }
  .photo--lips { background: linear-gradient(135deg, var(--photo-warm), #e8d2bd); }
  .photo--portrait { background: linear-gradient(160deg, #b08a6a, var(--photo-skin)); }
  .photo--eyes { background: linear-gradient(135deg, #8a7a5a, var(--photo-skin)); }
  .photo--glam { background: linear-gradient(180deg, #caa68a, #e6c7b3); }
</style>
</head>
<body>
  <section class="card card--front">
    <h1 class="brand">The Velvet Magpie</h1>
    <div class="identity">
      <p class="name">Marisol Dunkel</p>
      <p class="role">Professional Makeup Artist</p>
    </div>
    <ul class="contacts">
      <li>
        <svg viewBox="0 0 20 20" aria-hidden="true"><circle cx="10" cy="10" r="10" fill="var(--magenta)"/><path d="M7 5.5l2 2-1.2 1.3a6 6 0 0 0 3.4 3.4l1.3-1.2 2 2-1.3 1.5c-3.5-.3-7.2-4-7.5-7.5z" fill="#fff"/></svg>
        0471829304
      </li>
      <li>
        <svg viewBox="0 0 20 20" aria-hidden="true"><circle cx="10" cy="10" r="10" fill="var(--magenta)"/><rect x="5" y="6.5" width="10" height="7" fill="#fff"/><path d="M5 6.5l5 4 5-4" stroke="var(--magenta)" stroke-width="1.2" fill="none"/></svg>
        info@thevelvetmagpie.com
      </li>
      <li>
        <svg viewBox="0 0 20 20" aria-hidden="true"><circle cx="10" cy="10" r="10" fill="var(--magenta)"/><g stroke="#fff" stroke-width="1.1" fill="none"><circle cx="10" cy="10" r="5"/><ellipse cx="10" cy="10" rx="2.2" ry="5"/><path d="M5 10h10"/></g></svg>
        www.thevelvetmagpie.com
      </li>
      <li>
        <svg viewBox="0 0 20 20" aria-hidden="true"><circle cx="10" cy="10" r="10" fill="var(--magenta)"/></svg>
        / thevelvetmagpie
      </li>
    </ul>
    <div class="ornament" role="img" aria-label="Pink floral swirl ornament with scattered flowers"></div>
  </section>

  <section class="card card--back">
    <div class="collage">
      <div class="photo photo--party" role="img" aria-label="Bridesmaids in blue dresses holding white bouquets"></div>
      <div class="photo photo--lips" role="img" aria-label="Makeup artist applying lipstick to a blonde client"></div>
      <div class="photo photo--portrait" role="img" aria-label="Close-up portrait of a woman with finished makeup"></div>
      <div class="photo photo--eyes" role="img" aria-label="Makeup artist applying eye makeup to a client"></div>
      <div class="photo photo--glam" role="img" aria-label="Glamour portrait with red lipstick"></div>
    </div>
  </section>
</body>
</html>
```